Tech business card design

We need an amazing business card design for our new business 'Brakka' a marketing tech startup based in Sydney, Australia. We provide an online marketplace for businesses to search and buy advertising media, connect with service providers and learn more about marketing. We wish to communicate 'cool tech', reliability and professionalism and design based around our logo.

Target Market(s)

Business Owners

Contact Information for Business Card

Name
Position
Email Address
Website
Phone Number

Font styles to use
Other font styles liked:
• Avenir & Avenir Next

Colors

Designer to choose colors to be used in the design.

```html
<!DOCTYPE html>
<html lang="en">
<head>
<meta charset="utf-8">
<title>Brakka Business Card</title>
<link rel="stylesheet" href="https://fonts.googleapis.com/css2?family=Saira:wght@400;500;700;800&display=swap">
<style>
  :root {
    --backdrop: #7a5c3b;
    --navy: #11123f;
    --white: #ffffff;
    --paper-fade: #ededed;
    --rule: #8d8fae;
  }
  * { box-sizing: border-box; margin: 0; padding: 0; }
  html, body { width: 900px; height: 1200px; overflow: hidden; }
  body {
    position: relative;
    background: var(--backdrop);
    font-family: "Saira", sans-serif;
  }
  .card {
    position: absolute;
    left: 86px;
    width: 734px;
    height: 429px;
    border-radius: 22px;
    overflow: hidden;
  }
  .card-front {
    top: 131px;
    background: linear-gradient(to bottom, var(--white) 0, var(--white) 210px, var(--paper-fade) 290px);
  }
  .card-back { top: 633px; background: var(--navy); }

  .wordmark {
    position: absolute;
    left: 0; right: 0;
    text-align: center;
    font-family: "Saira", sans-serif;
    font-weight: 800;
    font-size: 128px;
    line-height: 1;
    letter-spacing: -2px;
  }
  .card-front .wordmark { top: 62px; color: var(--navy); }
  .card-back .wordmark { top: 147px; color: var(--white); }

  .holder {
    position: absolute;
    top: 222px; left: 0; right: 0;
    text-align: center;
    color: var(--navy);
  }
  .holder-name { font-weight: 700; font-size: 32px; line-height: 36px; letter-spacing: 0.5px; }
  .holder-role { font-weight: 500; font-size: 16px; line-height: 20px; }

  .rule-thin {
    position: absolute;
    top: 290px; left: 0; right: 0;
    height: 5px;
    background: var(--navy);
  }
  .contact-band {
    position: absolute;
    top: 300px; left: 0; right: 0; bottom: 0;
    background: var(--navy);
    color: var(--white);
    font-size: 17px;
    line-height: 25px;
    letter-spacing: 0.3px;
  }
  .address {
    position: absolute;
    top: 26px;
    right: 390px;
    text-align: right;
    font-style: normal;
  }
  .divider {
    position: absolute;
    left: 367px; top: 31px;
    width: 1px; height: 68px;
    background: var(--rule);
  }
  .channels {
    position: absolute;
    top: 26px; left: 388px;
    list-style: none;
  }
  .channels li { display: flex; align-items: center; height: 25px; }
  .channels svg { width: 16px; height: 16px; margin-right: 9px; flex: none; }
</style>
</head>
<body>

<section class="card card-front">
  <div class="wordmark">brakka</div>
  <div class="holder">
    <div class="holder-name">Liam Carter</div>
    <div class="holder-role">Managing Director</div>
  </div>
  <div class="rule-thin"></div>
  <div class="contact-band">
    <address class="address">18 Harbour Street<br>Level 6, Sydney<br>NSW 2000</address>
    <div class="divider"></div>
    <ul class="channels">
      <li>
        <svg viewBox="0 0 16 16" aria-hidden="true"><path fill="#fff" d="M3.2 1.5l2.4-.3 1.3 3.2-1.6 1.1c.8 1.8 2.2 3.2 4 4l1.1-1.6 3.2 1.3-.3 2.4c-.2.9-1 1.4-1.9 1.3C6.5 12.4 2.6 8.5 2 3.4c-.1-.9.4-1.7 1.2-1.9z"/></svg>
        +61 2 9012 4400
      </li>
      <li>
        <svg viewBox="0 0 16 16" aria-hidden="true"><rect x="1" y="3" width="14" height="10" fill="none" stroke="#fff" stroke-width="1.4"/><path d="M1 3l7 6 7-6M1 13l5-5M15 13l-5-5" fill="none" stroke="#fff" stroke-width="1.2"/></svg>
        info@brakka.com
      </li>
      <li>
        <svg viewBox="0 0 16 16" aria-hidden="true"><g fill="none" stroke="#fff" stroke-width="1.1"><circle cx="8" cy="8" r="6.5"/><ellipse cx="8" cy="8" rx="3" ry="6.5"/><path d="M1.5 8h13M2.5 4.8h11M2.5 11.2h11"/></g></svg>
        www.brakka.com
      </li>
    </ul>
  </div>
</section>

<section class="card card-back">
  <div class="wordmark">brakka</div>
</section>

</body>
</html>
```